Geschäftspapiere für Rechtsanwaltskanzlei
Zielgruppe
Rechtsanwaltskanzlei
Aufgabenstellung
Bitte inklusive Logo (sollte Recht, Digital/Apps, Medizin illustrieren) - habe das Preisgeld vor diesem Hintergrund erhöht.
Die Kanzlei arbeitet an der Schnittstelle von (Medizin-)Recht und Digital. Von daher wären wären Symbole/Gestaltung aus Bereich Medizin, Recht und Digital (z.B. Apps etc.) passend.
Das Briefpapier soll alle wichtigen Infos enthalten, aber dabei sehr klar gehalten werden und nicht überladen sein. Mir ist ein schlichtes und ansprechendes Design wichtig. Es soll nicht verspielt sein.
Info auf Briefpapier:
Kanzlei für Medizinrecht
Rechtsanwalt Dr. Lukas Brandl - Fachanwalt für Medizinrecht
Bitte Platzhalter/Freitextfelder für die anderen anderen Angaben, wie:
- Adresse
- Telefon-Nr.
- Homepage
- E-Mail
- Bankdaten.

```html
<!DOCTYPE html>
<html lang="de">
<head>
<meta charset="utf-8">
<title>Geschäftspapiere – Kanzlei Dr. Lukas Brandl</title>
<link href="https://fonts.googleapis.com/css2?family=Libre+Baskerville:wght@400;700&display=swap" rel="stylesheet">
<style>
  :root{
    --board:#333333;
    --paper:#ffffff;
    --envelope:#f0f1f3;
    --ink:#3f4750;
    --slate:#4b5a66;
    --blue:#4fa3dc;
    --blue-light:#88c8ee;
    --fold:#9c9c9c;
    --fold-light:#ababab;
    --shadow:rgba(0,0,0,.35);
  }
  *{margin:0;padding:0;box-sizing:border-box}
  html,body{width:1200px;height:840px;overflow:hidden;background:var(--board)}
  body{position:relative;font-family:"Libre Baskerville",Georgia,serif;color:var(--ink)}

  .sheet{position:absolute;background:var(--paper);box-shadow:6px 6px 8px var(--shadow);overflow:hidden}
  .letterhead{left:51px;top:71px;width:504px;height:713px}
  .letterhead .side-band{position:absolute;left:492px;top:35px;width:12px;height:127px;background:var(--blue-light)}
  .letterhead .foot-band{position:absolute;left:0;bottom:0;width:100%;height:12px;background:var(--blue-light)}
  .letterhead .fold-mark{position:absolute;left:9px;top:485px;width:10px;height:1px;background:var(--slate)}

  .brand{position:absolute;display:flex;align-items:center;gap:9px}
  .brand-square{width:20px;height:20px;background:var(--blue);flex:none}
  .brand-name{font-size:18px;color:var(--slate);white-space:nowrap}
  .tagline{position:absolute;font-size:8px;color:var(--slate);letter-spacing:.2px;white-space:nowrap}

  .letterhead .brand{left:100px;top:40px}
  .letterhead .tagline{left:141px;top:72px}

  .contact{position:absolute;left:376px;top:37px;font-size:6.4px;line-height:10.2px;color:var(--ink)}
  .contact h2{font-size:6.6px;font-weight:700;color:var(--blue);letter-spacing:.3px;margin-bottom:2px}
  .contact .label{color:var(--blue);display:inline-block;width:21px}
  .contact .rule{width:58px;height:1px;background:var(--blue);margin:8px 0 9px 22px}
  .contact .block{margin-bottom:5px}
  .contact .block + .block{margin-top:6px}
  .contact .key{color:var(--blue)}

  .envelope{background:var(--envelope)}
  .envelope svg.flap{position:absolute;left:0;top:0}
  .env-back-plain{left:642px;top:34px;width:493px;height:248px}
  .env-front{left:642px;top:303px;width:497px;height:249px}
  .env-back-band{left:648px;top:574px;width:493px;height:249px}
  .env-back-band .band{position:absolute;left:176px;top:0;width:136px;height:100%;background:var(--blue)}

  .return-address{position:absolute;left:0;width:100%;text-align:center;font-size:9.4px;color:var(--ink);letter-spacing:.1px}
  .env-back-plain .return-address{top:82px;padding-right:6px}
  .env-back-band .return-address{top:96px;padding-left:6px}

  .env-back-plain .brand,.env-back-band .brand{left:50%;transform:translateX(-50%);top:38px}
  .env-back-plain .brand{margin-left:-4px}
  .env-back-band .brand{margin-left:-2px}
  .env-back-band .brand-square{background:var(--slate)}
  .env-back-band .brand-name{color:var(--ink)}

  .env-front .brand{left:300px;top:170px}
  .env-front .tagline{left:341px;top:208px}
</style>
</head>
<body>

<section class="sheet letterhead" aria-label="Briefbogen">
  <div class="brand">
    <span class="brand-square"></span>
    <span class="brand-name">Dr. Lukas Brandl</span>
  </div>
  <p class="tagline">Fachanwalt für Medizinrecht</p>

  <div class="contact">
    <h2>KONTAKT</h2>
    <p><span class="label">Tel.</span>+49 000 000 47 3380</p>
    <p><span class="label">Fax.</span>+49 000 000 47 3381</p>
    <p><span class="label">Mail.</span>info@xxxxxx-lb.de</p>
    <p><span class="label">Web.</span>www.xxxxxx-lb.de</p>
    <div class="rule"></div>
    <div class="block">
      <p><span class="key">Bank:</span> Stadtbank Rheinau</p>
      <p>IBAN: DE XX 41020XX 2700004418</p>
      <p>BIC-Swift: RHNADEOOXXX</p>
    </div>
    <div class="block">
      <p>Amtsgericht Lindenau</p>
      <p>Handelsregister: 0000782</p>
      <p>USt.-ID-Nr.: DE0007820000</p>
    </div>
  </div>

  <span class="side-band"></span>
  <span class="fold-mark"></span>
  <span class="foot-band"></span>
</section>

<section class="sheet envelope env-back-plain" aria-label="Umschlag Rückseite">
  <svg class="flap" width="493" height="248" viewBox="0 0 493 248">
    <path d="M13 21 L238 172 Q248 179 258 173" fill="none" stroke="var(--fold)" stroke-width="1.6"/>
    <path d="M256 174 L478 30 Q488 22 491 8" fill="none" stroke="var(--fold)" stroke-width="3.5"/>
  </svg>
  <div class="brand">
    <span class="brand-square"></span>
    <span class="brand-name">Dr. Lukas Brandl</span>
  </div>
  <p class="return-address">AM LINDENHANG 14, 50823</p>
</section>

<section class="sheet envelope env-front" aria-label="Umschlag Vorderseite">
  <div class="brand">
    <span class="brand-square"></span>
    <span class="brand-name">Dr. Lukas Brandl</span>
  </div>
  <p class="tagline">Fachanwalt für Medizinrecht</p>
</section>

<section class="sheet envelope env-back-band" aria-label="Umschlag Rückseite mit Farbband">
  <span class="band"></span>
  <svg class="flap" width="493" height="249" viewBox="0 0 493 249">
    <path d="M13 22 L238 170 Q248 177 258 171" fill="none" stroke="var(--fold-light)" stroke-width="1.6"/>
    <path d="M256 172 L478 30 Q488 22 491 8" fill="none" stroke="var(--fold-light)" stroke-width="3.5"/>
  </svg>
  <div class="brand">
    <span class="brand-square"></span>
    <span class="brand-name">Dr. Lukas Brandl</span>
  </div>
  <p class="return-address">AM LINDENHANG 14, 50823</p>
</section>

</body>
</html>
```